certificate to present to patients after successful vasectomy

creation of a A4 sized colour certificate that can be presented to patients after their three month semen test confirms a successful vasectomy.
I have attached my current logo for Clearpath Vasectomy with the colours blue and green. I have attached a collage of example fun images related to congratulating men after their vasectomy.

Target Market(s)

A fun certificate to provide to men after a successful vasectomy. THis is a bit more playful/fun than traditional medical illustration/medical information. Men can stick it on the fridge or wave it about a family events to mortify their children.

Font styles to use
Sans Serif

Colors

Designer to choose colors to be used in the design.

Requirements
Must have
• Clearpath Vasectomy Logo and these or complimentary colours
• Be editable to add the patients name and date of certificate
Nice to have
• continuation of design themes from logo
Should not have
• should not have realistic or medical illustration of penis/scrotum. This should be a fun/silly certificate they can put on the family fridge or cork board

```html
<!DOCTYPE html>
<html lang="en">
<head>
<meta charset="utf-8">
<title>Vasectomy Success Certificate</title>
<link rel="stylesheet" href="https://fonts.googleapis.com/css2?family=Oswald:wght@700&family=Montserrat:wght@500;600&family=Great+Vibes&display=swap">
<style>
  :root {
    --page: #f6f9fb;
    --sky: #2a88c5;
    --teal: #4fa08f;
    --leaf: #8cc54e;
    --paper: #ffffff;
    --curl: #e3e6ea;
    --brand-blue: #1f80c8;
    --brand-green: #7dbb3a;
    --ink: #2d2d2d;
    --muted: #8b8b8b;
    --sun: #f2c23a;
  }
  * { margin: 0; padding: 0; box-sizing: border-box; }
  html, body { width: 1200px; height: 849px; overflow: hidden; background: var(--page); }
  .certificate { position: relative; width: 1200px; height: 849px; }
  .backdrop {
    position: absolute; left: 13px; top: 13px; right: 13px; bottom: 13px;
    background: linear-gradient(180deg, var(--sky) 0%, var(--teal) 45%, var(--leaf) 100%);
  }
  .sheet { position: absolute; left: 0; top: 0; }
  .badge {
    position: absolute; left: 544px; top: 184px; width: 100px; height: 100px;
    border-radius: 50%; background: var(--sun);
    border: 5px solid #f2f2f2; box-shadow: 0 3px 8px rgba(0,0,0,.2);
  }
  .headline {
    position: absolute; left: 0; width: 1190px; top: 318px; text-align: center;
    font-family: "Oswald", sans-serif; font-weight: 700; font-size: 56px; letter-spacing: 1px;
    background: repeating-linear-gradient(180deg, var(--brand-green) 0 2px, var(--sky) 2px 3px),
                linear-gradient(180deg, var(--brand-green), var(--sky));
    background-blend-mode: multiply;
    -webkit-background-clip: text; background-clip: text; color: transparent;
  }
  .patient-name {
    position: absolute; left: 0; width: 1190px; top: 410px; text-align: center;
    font-family: "Great Vibes", cursive; font-size: 84px; color: var(--brand-blue); line-height: 1.1;
  }
  .achievement {
    position: absolute; left: 0; width: 1190px; top: 530px; text-align: center;
    font-family: "Montserrat", sans-serif; font-weight: 600; font-size: 22px;
    letter-spacing: 2.4px; color: var(--muted);
  }
  .signature {
    position: absolute; left: 282px; top: 586px; width: 146px; height: 80px;
    background: linear-gradient(180deg, #fafafa, #f1f1f1); border-radius: 4px;
  }
  .signatory {
    position: absolute; left: 208px; width: 300px; top: 673px; text-align: center;
    font-family: "Montserrat", sans-serif; font-size: 19px; color: var(--ink);
  }
  .signatory strong { font-weight: 600; }
  .practice {
    position: absolute; left: 180px; width: 356px; top: 699px; text-align: center;
    font-family: "Montserrat", sans-serif; font-weight: 500; font-size: 19px; letter-spacing: .3px;
  }
  .practice .first { color: var(--brand-blue); }
  .practice .second { color: var(--brand-green); }
  .brand-mark {
    position: absolute; left: 900px; top: 648px; display: flex; align-items: center; gap: 8px;
    font-family: "Montserrat", sans-serif; font-weight: 600; font-size: 17px; line-height: 1.1;
    color: var(--brand-blue);
  }
  .brand-mark .square { width: 14px; height: 14px; background: var(--brand-blue); }
</style>
</head>
<body>
<main class="certificate">
  <div class="backdrop"></div>
  <svg class="sheet" width="1200" height="849" viewBox="0 0 1200 849" aria-hidden="true">
    <defs>
      <filter id="sheet-shadow" x="-5%" y="-5%" width="110%" height="115%">
        <feDropShadow dx="0" dy="4" stdDeviation="6" flood-color="#000" flood-opacity=".22"/>
      </filter>
    </defs>
    <path filter="url(#sheet-shadow)" fill="var(--paper)"
      d="M126,97 C300,92 420,110 560,104 C700,98 820,88 952,92 L1064,172 L1072,748
         C900,752 780,730 620,740 C460,750 330,756 210,742 C172,720 150,690 136,660 Z"/>
    <path fill="var(--curl)" d="M952,92 C985,100 1002,120 996,150 C1020,150 1048,158 1064,172 C1030,120 990,96 952,92 Z"/>
  </svg>

  <div class="badge" role="img" aria-label="Round yellow emoji sticker"></div>
  <h1 class="headline">CONGRATULATIONS!</h1>
  <p class="patient-name">John Doe</p>
  <p class="achievement">HAD A SUCCESSFUL VASECTOMY!</p>

  <div class="signature" role="img" aria-label="Doctor's handwritten signature"></div>
  <p class="signatory">Dr <strong>Martin Hale</strong></p>
  <p class="practice"><span class="first">CLEARPATH</span> <span class="second">VASECTOMY</span></p>

  <div class="brand-mark">
    <span class="square"></span>
    <span>CLEARPATH<br>VASECTOMY</span>
  </div>
</main>
</body>
</html>
```